Qorda - Web Design Rebrand for Talent Resourcing Company

I need a new brand for a customer based in Ireland.
The website currently: https://brevantic.io/
Tamwick repositioning themselves to be strategic talent resourcing and operational technology consultancy, Specialising in Life Sciences and Data Centres.
Essentially their USP:
They have lots of specialist manufacturing & automation resources that understand the Life Sciences Industry

Competitor websites:
https://vnrhublink.com/ I really like the clarity on this site and the pink/yellow mix could be replaced with a green/blue mix for Tamwick?
https://mrtovex.com/ These are a big company so anything we could steal would be good 😊

They want:
• Fresh, sharp imagery
• Movement on the main page (Rosalind is obsessed with this lol) so may be video on some sections?
• The facility to upload CVs so similar to above.
• A page to show types of jobs available
• A page to show types of resource available from Tamwick
• About us
• Sectors they operate in (includes Life Sciences, Food & Bev, Data Centres)

Target Market(s)

HR/Recruitment/Talent Acquisition/Operations Personnel in Life Sciences and Data Centres

Industry/Entity Type

Life Sciences and Data Centres

Number of Pages Required

1 page

Font styles to use
Sans Serif

Colors
0054AA
0677BA
7BADD7
CADEEF
E8F1F8
0094D4
00A9DD
6FCCEA
C7EBF8
E9F6FB
00AB8E
00BBA5
67D7C9
C6EFE9
E9F9F6

Requirements
Must have
• Brand Colour might be green/blue mix OR if another colour combo compelling
Nice to have
• Fresh, Sharp imagery. Movement on the main image (maybe partial video)

```html
<!DOCTYPE html>
<html lang="en">
<head>
<meta charset="utf-8">
<title>Tamwick — Strategic Talent Resourcing</title>
<link rel="stylesheet" href="https://fonts.googleapis.com/css2?family=Montserrat:wght@300;400;600;700&family=Inter:wght@400;500;600;700&display=swap">
<style>
  :root {
    --ink: #1b1b1b;
    --header-bg: #1c1c1c;
    --footer-bar: #262626;
    --brand-teal: #00AB8E;
    --brand-teal-light: #00BBA5;
    --brand-blue: #0054AA;
    --brand-blue-mid: #0677BA;
    --logo: #0d5a70;
    --soft-grey: #efefef;
    --white: #ffffff;
  }
  * { box-sizing: border-box; margin: 0; padding: 0; }
  html, body { width: 1200px; height: 3095px; overflow: hidden; background: var(--white); }
  body { position: relative; font-family: "Inter", Arial, sans-serif; color: var(--ink); }

  /* Header */
  .site-header { position: absolute; left: 0; top: 0; width: 1200px; height: 67px; background: var(--header-bg); }
  .site-header .brand { position: absolute; left: 127px; top: 14px; font-family: "Montserrat", sans-serif; font-weight: 700; font-size: 33px; color: var(--logo); letter-spacing: -0.5px; }
  .main-nav { position: absolute; left: 388px; top: 27px; display: flex; gap: 29px; font-size: 10px; color: #e8e8e8; }
  .upload-cv { position: absolute; left: 978px; top: 27px; font-size: 10px; color: #e8e8e8; text-decoration: underline; }
  .search-btn { position: absolute; left: 1045px; top: 18px; width: 30px; height: 30px; border: 1.5px solid var(--brand-teal); border-radius: 50%; }
  .search-btn svg { position: absolute; left: 8px; top: 8px; }

  /* Hero */
  .hero { position: absolute; left: 17px; top: 83px; width: 1166px; height: 730px; }
  .hero svg { position: absolute; left: 0; top: 0; }
  .hero-title { position: absolute; left: 0; top: 205px; width: 1166px; text-align: center; font-family: "Montserrat", sans-serif; font-weight: 300; font-size: 51px; line-height: 60px; color: var(--white); }
  .hero-sub { position: absolute; left: 0; top: 404px; width: 1166px; text-align: center; font-weight: 700; font-size: 16px; letter-spacing: 0.2px; color: var(--white); }

  /* About */
  .about-visual { position: absolute; left: 110px; top: 870px; }
  .about-copy { position: absolute; left: 672px; top: 910px; width: 405px; }
  .about-copy h2 { font-family: "Montserrat", sans-serif; font-weight: 400; font-size: 43px; margin-bottom: 26px; color: #1a1a1a; }
  .about-copy p { font-size: 12px; line-height: 20px; margin-bottom: 20px; color: #222; }
  .btn-pill { position: absolute; left: 672px; top: 1280px; width: 165px; height: 40px; border-radius: 20px; background: var(--brand-teal); color: var(--white); font-size: 11px; font-weight: 700; display: flex; align-items: center; justify-content: center; }

  /* Team */
  .team { position: absolute; left: 17px; top: 1420px; width: 1183px; height: 1167px; }
  .team-bg { position: absolute; left: 0; top: 0; }
  .team h2 { position: absolute; left: 108px; top: 190px; font-family: "Montserrat", sans-serif; font-weight: 400; font-size: 43px; color: var(--white); }
  .team-intro { position: absolute; left: 108px; top: 264px; width: 810px; font-size: 12.3px; line-height: 23px; color: var(--white); }
  .team-intro p + p { margin-top: 24px; }
  .featured-bar { position: absolute; left: 108px; top: 395px; width: 442px; height: 53px; background: linear-gradient(90deg, rgba(255,255,255,0.28), rgba(255,255,255,0)); color: var(--white); font-weight: 700; font-size: 18px; padding: 16px 0 0 53px; }
  .role-card { position: absolute; top: 502px; width: 545px; }
  .role-card .role-image { width: 545px; height: 338px; border-radius: 12px; }
  .role-card h3 { margin-top: 30px; font-family: "Montserrat", sans-serif; font-weight: 400; font-size: 26px; color: var(--white); }
  .role-card p { margin-top: 10px; width: 360px; font-size: 11px; line-height: 18px; color: var(--white); }
  .role-card .explore { position: absolute; left: 465px; top: 380px; }
  .img-meeting { background: linear-gradient(135deg, #3c4248, #1f2327 55%, #5c5247); }
  .img-lab { background: linear-gradient(120deg, #c7d8e3, #5d7c92 40%, #1d3a55 75%, #2bb9a1); }
  .slider-dots { position: absolute; left: 108px; top: 1034px; display: flex; gap: 15px; }
  .slider-dots span { width: 12px; height: 12px; border-radius: 50%; background: rgba(255,255,255,0.3); }
  .slider-dots span.active { background: var(--white); }

  /* Footer */
  .footer-brand { position: absolute; left: 127px; top: 2730px; font-family: "Montserrat", sans-serif; font-weight: 700; font-size: 60px; color: var(--logo); letter-spacing: -1px; }
  .social { position: absolute; left: 125px; top: 2837px; display: flex; gap: 17px; }
  .social span { width: 36px; height: 36px; border-radius: 50%; background: var(--brand-blue); }
  .social span:last-child { background: #111; }
  .footer-nav { position: absolute; left: 472px; top: 2697px; display: flex; flex-direction: column; gap: 24px; font-size: 13px; color: #111; line-height: 16px; }
  .stat { position: absolute; left: 690px; width: 383px; height: 82px; background: linear-gradient(90deg, var(--brand-blue), var(--brand-blue-mid) 45%, var(--brand-teal)); color: var(--white); }
  .stat .num { position: absolute; left: 38px; top: 17px; font-size: 40px; font-weight: 700; line-height: 48px; }
  .stat .divider { position: absolute; left: 138px; top: 28px; width: 1.5px; height: 26px; background: rgba(255,255,255,0.8); }
  .stat .label { position: absolute; left: 158px; top: 0; height: 82px; display: flex; align-items: center; width: 150px; font-size: 11px; line-height: 17px; }
  .copyright-bar { position: absolute; left: 0; top: 3033px; width: 1200px; height: 62px; background: var(--footer-bar); color: var(--white); font-size: 12.5px; display: flex; align-items: center; justify-content: center; }
</style>
</head>
<body>

<header class="site-header">
  <div class="brand">Tamwick</div>
  <nav class="main-nav">
    <span>Home</span><span>About Us</span><span>Capabilities</span><span>Our Clients</span><span>Join Our Team</span><span>Contact</span>
  </nav>
  <span class="upload-cv">Upload CV</span>
  <span class="search-btn">
    <svg width="12" height="12" viewBox="0 0 12 12"><circle cx="5" cy="5" r="3.5" fill="none" stroke="#cfcfcf" stroke-width="1.3"/><line x1="7.6" y1="7.6" x2="10.5" y2="10.5" stroke="#cfcfcf" stroke-width="1.3"/></svg>
  </span>
</header>

<section class="hero">
  <svg width="1166" height="730" viewBox="0 0 1166 730">
    <defs>
      <linearGradient id="heroPhoto" x1="0" y1="0" x2="1" y2="1">
        <stop offset="0" stop-color="#4a4a48"/>
        <stop offset="0.45" stop-color="#2a2a2a"/>
        <stop offset="0.8" stop-color="#3b3936"/>
        <stop offset="1" stop-color="#1c1c1c"/>
      </linearGradient>
      <path id="videoRing" d="M551 654 A45 45 0 1 1 615 654"/>
    </defs>
    <path class="hero-ribbon-blue" d="M140 716 C300 705 390 620 480 560 L520 552 C450 596 390 656 330 696 C270 726 200 730 140 716 Z" fill="var(--brand-blue-mid)"/>
    <path class="hero-ribbon-teal" d="M860 640 C940 700 1040 722 1166 660 V620 C1060 690 960 690 860 640 Z" fill="var(--brand-teal)"/>
    <ellipse class="hero-video-disc" cx="583" cy="610" rx="225" ry="110" fill="var(--soft-grey)"/>
    <path role="img" aria-label="Photo of a team of professionals collaborating around a laptop in a bright office"
      d="M0 0 H1166 V642 C1100 680 960 690 880 660 C820 635 760 560 680 545 C620 535 540 535 480 560 C380 600 300 700 116 713 C70 716 30 700 0 676 Z" fill="url(#heroPhoto)"/>
    <line x1="583" y1="487" x2="583" y2="559" stroke="#ffffff" stroke-width="1.2"/>
    <circle cx="583" cy="622" r="20" fill="#2f8fb3"/>
    <path d="M577 612 L592 622 L577 632 Z" fill="#ffffff"/>
    <text font-family="Inter, sans-serif" font-size="10" letter-spacing="3" fill="#1b1b1b">
      <textPath href="#videoRing">CLICK TO WATCH VIDEO</textPath>
    </text>
  </svg>
  <h1 class="hero-title">Strategic Talent Resourcing &amp;<br>Operational Technology<br>Export</h1>
  <p class="hero-sub">SPECIALISING IN LIFE SCIENCES AND DATA CENTRES</p>
</section>

<section class="about">
  <svg class="about-visual" width="520" height="500" viewBox="0 0 520 500">
    <defs>
      <linearGradient id="aboutPhoto" x1="0" y1="0" x2="1" y2="1">
        <stop offset="0" stop-color="#6b7278"/>
        <stop offset="0.5" stop-color="#d9d2c8"/>
        <stop offset="1" stop-color="#4a4440"/>
      </linearGradient>
    </defs>
    <path d="M330 20 C420 40 480 90 480 180 C485 260 470 330 420 400 C380 460 300 485 220 478 L300 470 C380 420 430 300 420 220 Z" fill="var(--brand-blue)"/>
    <path d="M20 200 C30 90 120 20 240 15 C180 30 80 90 40 190 Z" fill="var(--brand-teal)"/>
    <circle role="img" aria-label="Photo of a smiling young professional taking notes at a meeting table with a colleague behind" cx="248" cy="243" r="232" fill="url(#aboutPhoto)"/>
  </svg>
  <div class="about-copy">
    <h2>About Tamwick</h2>
    <p>Tamwick is proud to be providing top-tier resources to the life sciences sector, specialising in delivering high-quality talent and solutions that enhance the capabilities and operational excellence of our customers.</p>
    <p>Our operational technology expertise and talent pool has evolved over the past decade with successful project delivery for numerous life sciences organisations , so we are uniquely positioned to understand and meet your requirements.</p>
    <p>We are focused on matching the dynamic needs of life sciences firms with skilled professionals, thereby driving innovation and growth in this critical sector across Ireland.</p>
  </div>
  <span class="btn-pill">Read More</span>
</section>

<section class="team">
  <svg class="team-bg" width="1166" height="1167" viewBox="0 0 1166 1167">
    <defs>
      <linearGradient id="teamGrad" x1="0" y1="0" x2="1" y2="1">
        <stop offset="0" stop-color="var(--brand-teal)"/>
        <stop offset="0.55" stop-color="#0483a8"/>
        <stop offset="1" stop-color="var(--brand-blue)"/>
      </linearGradient>
    </defs>
    <path d="M0 18 C90 -8 220 5 340 55 C430 92 520 100 620 70 C760 28 900 -10 1040 10 C1100 18 1140 20 1166 15 V1167 H0 Z" fill="url(#teamGrad)"/>
  </svg>
  <h2>Meet Our Team</h2>
  <div class="team-intro">
    <p>Tamwick employees have a variety of skills and experience, but they all are professional, experienced in their field and enjoy the variety of working at different client sites over time.</p>
    <p>They get a feeling of success seeing a project through to completion, and are always willing to go the extra mile for our clients.</p>
  </div>
  <div class="featured-bar">Featured roles</div>

  <article class="role-card" style="left:108px;">
    <div class="role-image img-meeting" role="img" aria-label="Photo of business people meeting around a conference table"></div>
    <h3>Automation &amp; CSV</h3>
    <p>Lorem Ipsum is simply dummy text of the printing and typesetting industry. Lorem Ipsum has been the industry's standard dummy text ever since the 1500s,</p>
    <svg class="explore" width="72" height="72" viewBox="0 0 72 72">
      <defs><path id="exploreRing1" d="M14 52 A26 26 0 1 1 58 52"/></defs>
      <text font-family="Inter, sans-serif" font-size="7.5" letter-spacing="1.2" fill="#ffffff"><textPath href="#exploreRing1">Explore To Learn More</textPath></text>
      <path d="M30 42 L42 30 M34 30 H42 V38" stroke="#ffffff" stroke-width="1.6" fill="none"/>
    </svg>
  </article>

  <article class="role-card" style="left:675px;">
    <div class="role-image img-lab" role="img" aria-label="Photo of a scientist in a mask holding a glowing molecular network graphic"></div>
    <h3>Bioprocess</h3>
    <p>Lorem Ipsum is simply dummy text of the printing and typesetting industry. Lorem Ipsum has been the industry's standard dummy text ever since the 1500s,</p>
    <svg class="explore" width="72" height="72" viewBox="0 0 72 72">
      <defs><path id="exploreRing2" d="M14 52 A26 26 0 1 1 58 52"/></defs>
      <text font-family="Inter, sans-serif" font-size="7.5" letter-spacing="1.2" fill="#ffffff"><textPath href="#exploreRing2">Explore To Learn More</textPath></text>
      <path d="M30 42 L42 30 M34 30 H42 V38" stroke="#ffffff" stroke-width="1.6" fill="none"/>
    </svg>
  </article>

  <div class="slider-dots"><span class="active"></span><span></span><span></span><span></span><span></span></div>
</section>

<footer>
  <div class="footer-brand">Tamwick</div>
  <div class="social"><span></span><span></span><span></span></div>
  <nav class="footer-nav">
    <span>Home</span><span>About Us</span><span>Capabilities</span><span>Our Clients</span><span>Join Our Team</span><span>Contact</span>
  </nav>
  <div class="stat" style="top:2670px;"><span class="num">50+</span><span class="divider"></span><span class="label">Number skilled<br>automation engineers</span></div>
  <div class="stat" style="top:2763px;"><span class="num">25+</span><span class="divider"></span><span class="label">Customers currently<br>using Tamwick</span></div>
  <div class="stat" style="top:2858px;"><span class="num" style="left:32px;">99%</span><span class="divider"></span><span class="label">Customer retention</span></div>
  <div class="copyright-bar">Copyright 2024-Tamwick-All rights reserved</div>
</footer>

</body>
</html>
```